Inspirational speaker and coach Corinne Valbeck is building a website

Design, Create and launch a 10-15 page Wordpress website. Please research Corinne online and use examples you have access to.

```html
<!DOCTYPE html>
<html lang="en">
<head>
<meta charset="utf-8">
<title>Corinne Valbeck — Brand Specialist</title>
<link href="https://fonts.googleapis.com/css2?family=Poppins:wght@300;400;500;600;700&family=Lora:wght@400;500&display=swap" rel="stylesheet">
<style>
:root{
  --yellow:#f8d02f;
  --gold:#eebe2b;
  --orange:#e0502d;
  --ink:#111;
  --text:#333;
  --muted:#777;
  --dark:#1b1b1b;
  --footer:#2a2a2c;
  --white:#fff;
}
*{margin:0;padding:0;box-sizing:border-box}
html,body{width:1200px;height:4871px;overflow:hidden}
body{position:relative;font-family:"Poppins",sans-serif;color:var(--text);background:var(--white)}
.abs{position:absolute}
.serif{font-family:"Lora",serif}
.photo{position:absolute}

/* header */
.site-header{position:absolute;left:0;top:0;width:1200px;height:82px;background:var(--white)}
.brand{position:absolute;left:47px;top:26px;font-size:22px;font-weight:600;color:#222;display:flex;align-items:center;gap:8px}
.brand .dot{width:10px;height:10px;border-radius:50%;background:var(--gold)}
.brand .first{color:var(--gold)}
.nav{position:absolute;top:29px;left:462px;display:flex;gap:27px;font-size:16px;font-weight:500;color:#222}
.nav .active{color:var(--gold)}
.btn-contact{position:absolute;left:1008px;top:22px;width:145px;height:40px;border-radius:20px;background:#111;color:#fff;font-size:14px;font-weight:600;display:flex;align-items:center;justify-content:center}

/* hero */
.hero{position:absolute;left:0;top:82px;width:1200px;height:545px;background:linear-gradient(90deg,#6e5e48 0%,#766450 50%,#8a7761 100%)}
.hero .photo{left:600px;top:0;width:600px;height:545px;background:radial-gradient(ellipse at 60% 40%,#b69a7a 0%,#8b7358 45%,#73624c 100%)}
.hero h1{position:absolute;left:42px;top:130px;font-size:68px;font-weight:700;color:#fff;line-height:1}
.hero h1 span{color:var(--gold)}
.hero h2{position:absolute;left:42px;top:212px;font-size:34px;font-weight:500;color:#fff}
.hero p{position:absolute;left:42px;top:282px;width:560px;font-size:18px;line-height:28px;color:#fff}

/* intro */
.video-box{left:42px;top:737px;width:344px;height:344px;background:linear-gradient(160deg,#3a3a3a,#161616)}
.play{position:absolute;left:24px;top:265px;width:54px;height:54px;border-radius:50%;background:var(--orange)}
.video-box .label{position:absolute;left:100px;top:268px;color:#fff;font-size:19px;font-weight:500;line-height:24px}
.video-box .label small{display:block;font-size:14px;font-weight:400;color:#ddd}
.quote-mark{left:520px;top:690px;font-family:"Lora",serif;font-size:330px;line-height:1;color:#ececec}
.intro-title{left:451px;top:735px;width:720px;font-size:36px;line-height:42px;color:#222}
.feature{position:absolute;width:290px}
.feature svg{position:absolute;left:0;top:0}
.feature h3{position:absolute;left:85px;top:0;font-size:17px;font-weight:600;color:#111}
.feature p{position:absolute;left:85px;top:28px;width:240px;font-size:14px;line-height:22px;color:#666}

.tab-yellow{left:38px;width:346px;height:118px;background:var(--yellow);padding:28px 0 0 42px;font-size:21px;font-weight:600;line-height:29px;color:#111}

/* dark band */
.about-band{left:0;top:1273px;width:1200px;height:455px;background:#0c0c0c}
.about-band .photo{left:560px;top:0;width:640px;height:455px;background:radial-gradient(ellipse at 40% 50%,#4a4540 0%,#1d1c1b 55%,#0c0c0c 100%)}
.about-menu{left:38px;top:0;width:346px;height:190px;background:#1d1d1d}
.about-menu li{list-style:none;position:absolute;left:44px;font-size:16px;font-weight:500;color:#fff}
.about-menu .bar{position:absolute;left:0;top:141px;width:5px;height:49px;background:var(--orange)}
.about-band h2{position:absolute;left:50px;top:250px;font-size:34px;font-weight:400;color:#fff;letter-spacing:1px}
.about-band p{position:absolute;left:50px;top:318px;width:480px;font-size:17px;line-height:29px;color:#fff}

/* events */
.events-title{left:56px;top:1840px;font-size:36px;font-weight:700;color:#111}
.events-desc{left:56px;top:1905px;width:340px;font-size:20px;line-height:31px;color:#777}
.events-link{left:56px;top:2025px;font-size:18px;color:#111;border-bottom:2px solid var(--yellow);padding-bottom:3px}
.event-card{position:absolute;top:1822px;width:219px;height:309px}
.event-card span{position:absolute;left:26px;bottom:38px;color:#fff;font-size:16px;font-weight:500;line-height:18px}

/* schedule */
.schedule{left:0;top:2225px;width:1200px;height:125px;background:var(--yellow)}
.schedule p{position:absolute;left:52px;top:44px;font-size:27px;font-weight:600;color:#111;letter-spacing:-.5px}
.btn-appoint{position:absolute;left:925px;top:30px;width:217px;height:65px;border-radius:33px;background:#0d0d0d;color:var(--yellow);font-size:17px;font-weight:600;display:flex;align-items:center;justify-content:center}

/* expertise */
.expert-title{left:60px;top:2393px;width:620px;font-size:36px;line-height:42px;color:#222}
.circle{position:absolute;border-radius:50%;background:linear-gradient(180deg,#eef4f7 0%,#d9e7ee 100%)}
.expert-card{position:absolute;background:#fff;box-shadow:0 8px 30px rgba(0,0,0,.06)}
.expert-card h3{position:absolute;left:75px;top:40px;font-size:17px;font-weight:600;color:#111}
.expert-card p{position:absolute;left:75px;top:72px;width:260px;font-size:15px;line-height:26px;color:#777}
.expert-icon{position:absolute;width:56px;height:56px;display:flex;align-items:center;justify-content:center}

/* testimonial */
.testimonial{left:0;top:3085px;width:1200px;height:615px;background:linear-gradient(90deg,#2f3b30 0%,#46563f 45%,#3a4634 70%,#263024 100%)}
.testimonial .photo-main{position:absolute;left:560px;top:0;width:420px;height:615px;background:radial-gradient(ellipse at 50% 45%,#6a6459 0%,#3f4a39 60%,rgba(0,0,0,0) 100%)}
.thumb{position:absolute;left:38px;width:346px}
.thumb .who{position:absolute;left:34px;top:60px;color:#fff;font-size:17px;font-weight:600;line-height:22px}
.thumb .who small{display:block;font-size:13px;font-weight:400}
.testimonial blockquote{position:absolute;left:426px;top:140px;width:730px;font-family:"Lora",serif;font-size:30px;line-height:40px;color:#fff}
.testimonial .author{position:absolute;left:426px;top:440px;color:#fff;font-size:20px;font-weight:600}
.testimonial .author small{display:block;font-size:15px;font-weight:400}

/* news */
.news-title{left:56px;top:3788px;font-size:36px;font-weight:700;color:#111}
.news-card{position:absolute;top:3888px;width:344px;height:480px;background:#fff;box-shadow:0 6px 24px rgba(0,0,0,.06)}
.news-card .photo{left:0;top:0;width:344px;height:182px}
.news-date{position:absolute;left:274px;top:142px;width:48px;text-align:center}
.news-date b{display:block;background:#fff;font-size:26px;font-weight:600;color:#111;line-height:44px}
.news-date i{display:block;font-style:normal;background:var(--yellow);font-size:12px;font-weight:600;color:#111;line-height:20px}
.news-card h3{position:absolute;left:33px;top:218px;width:290px;font-size:20px;font-weight:600;line-height:25px;color:#111}
.news-card p{position:absolute;left:33px;top:278px;width:290px;font-size:15px;line-height:26px;color:#777}

/* footer */
.site-footer{left:0;top:4490px;width:1200px;height:381px;background:var(--footer);color:#fff}
.site-footer .brand{left:47px;top:84px;color:#fff}
.footer-tag{position:absolute;left:50px;top:130px;font-family:"Lora",serif;font-size:16px;color:#8a8a8a}
.social{position:absolute;top:166px;width:30px;height:30px;border-radius:4px}
.footer-col h4{position:absolute;top:86px;font-size:19px;font-weight:500;color:#fff}
.hours{position:absolute;left:281px;top:126px;font-family:"Lora",serif;font-size:16px;line-height:35px;color:#8a8a8a}
.subscribe{position:absolute;left:711px;top:130px;width:447px;height:50px;border-radius:25px;background:#fff}
.subscribe span{position:absolute;left:22px;top:15px;font-family:"Lora",serif;font-size:15px;color:#999}
.subscribe b{position:absolute;right:0;top:0;width:170px;height:50px;border-radius:25px;background:var(--yellow);color:#111;font-size:15px;font-weight:600;display:flex;align-items:center;justify-content:center}
.footer-rule{position:absolute;left:0;top:285px;width:1200px;height:1px;background:#3d3d3f}
.footer-links{position:absolute;left:52px;top:320px;display:flex;gap:37px;font-size:16px;color:#9a9a9a}
.copyright{position:absolute;right:48px;top:320px;font-family:"Lora",serif;font-size:16px;color:#6e6e6e}
</style>
</head>
<body>

<header class="site-header">
  <div class="brand"><span class="dot"></span><span><span class="first">Corinne</span> Valbeck</span></div>
  <nav class="nav"><span class="active">Home</span><span>About Me</span><span>Courses</span><span>Events</span><span>Clients</span><span>Blog</span></nav>
  <div class="btn-contact">CONTACT ME</div>
</header>

<section class="hero">
  <div class="photo" role="img" aria-label="Portrait of the speaker holding a jewelled crown toward the camera"></div>
  <h1><span>Corinne</span> Valbeck</h1>
  <h2>Brand Specialist</h2>
  <p>I am an experienced and seasoned business executive with expertise in operations, administration and management for multimillion-dollar companies.</p>
</section>

<section class="intro">
  <div class="abs video-box" role="img" aria-label="Close-up of a studio microphone in low light">
    <div class="play"><svg width="54" height="54" viewBox="0 0 54 54"><path d="M22 17 L37 27 L22 37 Z" fill="#fff"/></svg></div>
    <div class="label">Motivate you<small>Experience</small></div>
  </div>
  <div class="abs quote-mark">“</div>
  <h2 class="abs intro-title serif">I get you motivated to be the best you can be in everything you do.</h2>

  <div class="feature" style="left:466px;top:945px">
    <svg width="60" height="56" viewBox="0 0 60 56" fill="none" stroke="#e58a6b" stroke-width="2"><path d="M6 10h46l-6 10H12z"/><path d="M14 20v10M28 20v10M42 20v10"/><circle cx="10" cy="38" r="5"/><circle cx="24" cy="38" r="5"/><circle cx="38" cy="38" r="5"/><circle cx="52" cy="38" r="5"/></svg>
    <h3>SPECHES</h3><p>Firms that allow customers to transfer risk for a fee.</p>
  </div>
  <div class="feature" style="left:818px;top:945px">
    <svg width="60" height="56" viewBox="0 0 60 56" fill="none" stroke="#e58a6b" stroke-width="2"><path d="M4 10h20c4 0 6 3 6 6v32c0-3-2-5-6-5H4z"/><path d="M56 10H36c-4 0-6 3-6 6v32c0-3 2-5 6-5h20z"/></svg>
    <h3>MY BOOKS</h3><p>Providing advice and ways to put money to work.</p>
  </div>
  <div class="feature" style="left:466px;top:1065px">
    <svg width="60" height="56" viewBox="0 0 60 56" fill="none" stroke="#e58a6b" stroke-width="2"><path d="M10 16l24-8 14 30-24 10z"/><path d="M6 22l18 28M14 12l20 34"/></svg>
    <h3>ARTICLES</h3><p>Representing the commercial interests of a client for a fee.</p>
  </div>
  <div class="feature" style="left:818px;top:1065px">
    <svg width="60" height="56" viewBox="0 0 60 56" fill="none" stroke="#e58a6b" stroke-width="2"><rect x="4" y="10" width="52" height="34"/><path d="M26 20l10 7-10 7z"/></svg>
    <h3>VIDEO &amp; AUDIO</h3><p>Providing tutoring or professional training.</p>
  </div>

  <div class="abs tab-yellow" style="top:1155px">BEFORE YOU PROCEED<br>KNOW WHO AM I ?</div>
</section>

<section class="abs about-band">
  <div class="photo" role="img" aria-label="The speaker holding a crown beside a glowing motivational sign on a dark background"></div>
  <ul class="abs about-menu">
    <li style="top:20px">BIOGRAPHY</li>
    <li style="top:84px">PRESS RELESE</li>
    <li style="top:148px">GALLERY</li>
    <span class="bar"></span>
  </ul>
  <h2 class="serif">TYPES OF BUSINESS</h2>
  <p>I possess a strong strategic vision with ability to pinpoint and resolve complex dynamic</p>
</section>

<section class="events">
  <h2 class="abs events-title">EVENTS</h2>
  <p class="abs events-desc serif">Organizing and promoting events such as concerts or business conferences.</p>
  <span class="abs events-link">all events</span>
  <div class="event-card" style="left:428px;background:linear-gradient(180deg,#dfe8ee 0%,#b9c3c9 55%,#3a3a3a 100%)" role="img" aria-label="Desk with planning notes and sticky labels"><span>PROFESSIONAL<br>SERVICES</span></div>
  <div class="event-card" style="left:675px;background:linear-gradient(180deg,#6b5a4a 0%,#5a4a3c 55%,#221c17 100%)" role="img" aria-label="Two people shaking hands over a laptop"><span>CONSULTING</span></div>
  <div class="event-card" style="left:923px;background:linear-gradient(180deg,#c9c2b6 0%,#8d7e6c 55%,#2a241e 100%)" role="img" aria-label="Colleagues giving a high five"><span>COMMUNICATION</span></div>
</section>

<section class="abs schedule">
  <p>Schedule a coaching, speaking, or training engagement</p>
  <div class="btn-appoint">APPOINTMENT</div>
</section>

<section class="expertise">
  <h2 class="abs expert-title serif">Business is the process of creating and capturing value.</h2>
  <div class="circle" style="left:52px;top:2470px;width:340px;height:340px"></div>
  <div class="circle" style="left:705px;top:2450px;width:500px;height:500px"></div>

  <div class="expert-card" style="left:205px;top:2575px;width:357px;height:155px"><h3>EXPERT IN LEADERSHIP</h3><p>Selling goods and services from a physical shop.</p></div>
  <div class="expert-icon" style="left:176px;top:2627px;background:#e9a58c"><svg width="26" height="20" viewBox="0 0 26 20" fill="none" stroke="#fff" stroke-width="2"><rect x="1" y="1" width="24" height="18"/><path d="M5 7h7M5 12h7M15 6h6v8h-6z"/></svg></div>

  <div class="expert-card" style="left:660px;top:2575px;width:335px;height:130px"><h3>EXPERT IN SALES</h3><p style="width:240px">This may result in premium items that can compete on quality.</p></div>
  <div class="expert-icon" style="left:630px;top:2637px;background:#e8be4a"><svg width="20" height="24" viewBox="0 0 20 24" fill="none" stroke="#fff" stroke-width="2"><rect x="1" y="1" width="18" height="22"/><path d="M5 16h10"/></svg></div>

  <div class="expert-card" style="left:425px;top:2790px;width:348px;height:157px"><h3>TRAIN YOUR TEAM</h3><p style="width:220px">Manufacturing goods to specifications for a fee.</p></div>
  <div class="expert-icon" style="left:398px;top:2840px;background:#8ecae8"><svg width="26" height="20" viewBox="0 0 26 20" fill="none" stroke="#fff" stroke-width="2"><rect x="1" y="1" width="24" height="18"/><path d="M5 7h7M5 12h7M15 6h6v8h-6z"/></svg></div>

  <div class="abs tab-yellow" style="top:2968px">CUSTOMERS SHARING<br>EXPERIANCE WITH ME</div>
</section>

<section class="abs testimonial">
  <div class="photo-main" role="img" aria-label="Bearded man in a leather jacket standing in a forest"></div>
  <div class="thumb" style="top:0;height:150px;background:linear-gradient(180deg,#4d4a44,#2c2b28)" role="img" aria-label="Man in a suit in front of a building"></div>
  <div class="thumb" style="top:150px;height:145px;background:linear-gradient(180deg,#4e5b46,#2a3226)" role="img" aria-label="Man in a leather jacket outdoors">
    <div class="who">MARCUS ELLERY<small>American novelist</small></div>
  </div>
  <div class="thumb" style="top:295px;height:152px;background:linear-gradient(180deg,#5a3e28,#1f150d)" role="img" aria-label="Man reading at a desk">
    <svg class="abs" style="left:160px;top:82px" width="26" height="16" viewBox="0 0 26 16" fill="none" stroke="#fff" stroke-width="2"><path d="M2 2l11 11L24 2"/></svg>
  </div>
  <blockquote>In our lives, there are many incredible people who inspire and mold our character and future. These mentors and leaders come in all shapes and forms, never failing to provide motivation and advice. For a great number of people, such inspiration comes in the form of a coach or trainer.</blockquote>
  <div class="author">MARCUS ELLERY<small>American novelist</small></div>
</section>

<section class="news">
  <h2 class="abs news-title">LATEST NEWS</h2>
  <article class="news-card" style="left:56px">
    <div class="photo" style="background:linear-gradient(135deg,#cfc7bd,#7d7266)" role="img" aria-label="Team meeting around a whiteboard"></div>
    <div class="news-date"><b>04</b><i>JAN</i></div>
    <h3>Seven Facts You Never Knew About Business.</h3>
    <p>God may his. Lesser second abundantly multiply void also said doesn't grass. Divided may gathering light midst light our created said won't us lesser whose likeness midst one that deep.</p>
  </article>
  <article class="news-card" style="left:428px;height:473px">
    <div class="photo" style="background:linear-gradient(135deg,#7a6655,#3c2f25)" role="img" aria-label="Handshake over a desk with a laptop"></div>
    <div class="news-date"><b>04</b><i>JAN</i></div>
    <h3>Looking back on 2018 + my goals for 2019</h3>
    <p>Creepeth beginning without said. Without the void land. Day creeping deep abundantly rule open thing moveth creeping moved morning night likeness image grass seasons lesser be his, seed, us dry.</p>
  </article>
  <article class="news-card" style="left:800px;height:445px">
    <div class="photo" style="background:linear-gradient(135deg,#4c5a6a,#2a2f36)" role="img" aria-label="Woman presenting to a group in a bright office"></div>
    <div class="news-date"><b>04</b><i>JAN</i></div>
    <h3>Tips for mental sharpness and mommy brain</h3>
    <p>Fly brought fifth one it fourth kind, fly night, from. Dry above darkness make dry. Which lights, thing spirit. Was fruit firmament. Creeping set him great. Also under. Third isn't.</p>
  </article>
</section>

<footer class="abs site-footer">
  <div class="brand"><span class="dot"></span><span><span class="first">Corinne</span> Valbeck</span></div>
  <div class="footer-tag">Business Coach</div>
  <span class="social" style="left:52px;background:#2f5fb3"></span>
  <span class="social" style="left:104px;background:#2aa3e6"></span>
  <span class="social" style="left:156px;border:2px solid #bbb;border-radius:50%"></span>
  <div class="footer-col"><h4 style="left:281px">WORKING HOURS</h4></div>
  <div class="hours">Monday – Thursday: 0600 – 1800 hrs<br>Friday &amp; Saturday: 0600 – 0900 hrs<br>And all the Sundays Will be Holidays</div>
  <div class="footer-col"><h4 style="left:711px">SUBSCRIBE NEWSLETTER</h4></div>
  <div class="subscribe"><span>Email address</span><b>SUBSCRIBE</b></div>
  <div class="footer-rule"></div>
  <nav class="footer-links"><span>Home</span><span>Courses</span><span>Portfolio</span><span>Events</span><span>Blog</span><span>Contact</span></nav>
  <div class="copyright">© 2021, Corinne Valbeck. All Rights Reserved.</div>
</footer>

</body>
</html>
```